R7 Web Design Project

New company website for Intel cyber security company.

Style should be cool, but remain appropriate for very serious subject matter and audience.

Target Market(s)

Target audience is government and the military

Navigation needs to include:
- About Us
- Services
- Careers
- Contact Us
- Contracts

As well as 2 feature areas - use "Technology Integration" and "Case Study" as the supporting headlines.

Industry/Entity Type

Security

Font styles to use
Sans Serif

Colors

Designer to choose colors to be used in the design.

Requirements
Must have
• Mountain imagery and theme.

Use logo attached.

New Tagline - "Securing the Continuum"
Nice to have
• Supporting imagery could include photos representative of security - avoid cliches.
Should not have
• Needs to be serious not frivolous

```html
<!DOCTYPE html>
<html lang="en">
<head>
<meta charset="utf-8">
<title>R7 GROUP</title>
<link href="https://fonts.googleapis.com/css2?family=Cantarell&family=Oswald:wght@300&family=Arimo:wght@400;700&display=swap" rel="stylesheet">
<style>
  :root {
    --navy: #1d2e7a;
    --navy-text: #1e2f78;
    --ink: #222;
    --muted: #666;
    --nav-bg: #e2e2e2;
    --panel-bg: #e7e7e8;
    --box-bg: #f4f4f4;
    --rule: #c9c9c9;
    --white: #fff;
  }
  * { margin: 0; padding: 0; box-sizing: border-box; }
  html, body { width: 960px; height: 1200px; overflow: hidden; background: var(--white); }
  body { position: relative; font-family: "Arimo", Arial, sans-serif; color: var(--ink); }
  .abs { position: absolute; }
  .heading { font-family: "Cantarell", sans-serif; color: var(--navy-text); font-weight: 400; }
  .lines { white-space: nowrap; }

  /* Brand */
  .brand-mark { left: 334px; top: 12px; width: 72px; height: 71px; background: var(--navy); }
  .brand-name { left: 420px; top: 22px; font-family: "Cantarell", sans-serif; font-size: 42px; line-height: 50px; color: var(--navy-text); }

  /* Navigation */
  .main-nav { left: 62px; top: 96px; width: 836px; height: 39px; background: var(--nav-bg); border-top: 2px solid #d0d0d0; border-bottom: 2px solid #d0d0d0; }
  .main-nav a { position: absolute; top: 9px; font-family: "Cantarell", sans-serif; font-size: 13.5px; color: #333; text-decoration: none; }
  .main-nav a.current { color: var(--navy-text); }
  .search { position: absolute; left: 598px; top: 9px; display: flex; align-items: center; gap: 6px; font-size: 11px; color: #777; }

  /* Hero */
  .hero { left: 62px; top: 142px; width: 836px; height: 292px; overflow: hidden;
    background: linear-gradient(160deg, #3c62ad 0%, #6f8fc6 30%, #9fb5da 55%, #5b7fbf 75%, #2a4f9c 100%); }
  .hero-title { position: absolute; left: 0; width: 836px; top: 80px; text-align: center; font-family: "Oswald", sans-serif; font-weight: 300; font-size: 31px; line-height: 36px; color: var(--white); letter-spacing: -0.3px; }
  .hero-rule { position: absolute; left: 265px; top: 122px; width: 309px; height: 1px; background: rgba(255,255,255,0.85); }
  .hero-text { position: absolute; left: 269px; top: 129px; font-size: 10.6px; line-height: 18.3px; color: var(--white); letter-spacing: 0.6px; }
  .hero-arrow { position: absolute; top: 116px; }
  .hero-dots { position: absolute; top: 263px; left: 373px; display: flex; gap: 10px; }
  .hero-dots span { width: 15px; height: 15px; border-radius: 50%; background: #e8e8e8; border: 2px solid #fff; box-shadow: 0 0 2px rgba(0,0,0,.4); }
  .hero-dots span.active { background: #444; }

  /* Welcome */
  .welcome-title { left: 0; width: 960px; top: 445px; text-align: center; font-size: 22px; line-height: 28px; }
  .welcome-text { left: 182px; top: 480px; font-size: 11.4px; line-height: 18.4px; }
  .welcome-note { left: 225px; top: 539px; font-size: 9.3px; line-height: 18.4px; color: var(--muted); letter-spacing: 0.7px; }

  /* Features */
  .features { left: 62px; top: 593px; width: 836px; height: 241px; background: var(--panel-bg); border: 1px solid #cfcfcf; }
  .features-title { position: absolute; left: 0; width: 834px; top: 25px; text-align: center; font-size: 20px; line-height: 26px; }
  .feature-photo { position: absolute; top: 65px; width: 183px; height: 109px; background: var(--white); padding: 4px; box-shadow: 0 0 2px rgba(0,0,0,.25); }
  .feature-photo div { width: 100%; height: 100%; }
  .photo-security { background: linear-gradient(135deg, #0b1c6e, #1f5fd6 50%, #0b1c6e); }
  .photo-meeting { background: linear-gradient(90deg, #2a2a2a, #d9d9d9 45%, #3a3a3a 75%, #bdbdbd); }
  .feature-title { position: absolute; top: 67px; font-size: 16px; line-height: 20px; }
  .feature-text { position: absolute; top: 97px; font-size: 10px; line-height: 18.3px; color: var(--muted); letter-spacing: 0.5px; }
  .read-more { position: absolute; top: 174px; width: 110px; height: 33px; background: var(--navy); color: var(--white); font-family: "Cantarell", sans-serif; font-size: 12.5px; text-align: center; line-height: 33px; }

  /* News */
  .news-title { left: 72px; top: 843px; font-size: 20px; line-height: 26px; }
  .news-list { left: 70px; top: 880px; width: 404px; list-style: none; }
  .news-list li { border-bottom: 1px solid var(--rule); padding: 2px 0 3px 2px; }
  .news-date { display: block; font-size: 10px; color: var(--muted); line-height: 18px; }
  .news-text { display: block; font-size: 10.8px; line-height: 18.4px; }

  /* Newsletter */
  .newsletter { left: 568px; top: 857px; width: 330px; height: 232px; background: var(--box-bg); border: 1px solid #cfcfcf; }
  .newsletter h2 { position: absolute; left: 79px; top: 15px; font-size: 17.5px; line-height: 22px; }
  .newsletter label { position: absolute; left: 81px; font-size: 11px; line-height: 13px; color: #333; }
  .newsletter .field { position: absolute; left: 79px; width: 192px; height: 25px; background: var(--white); border: 1px solid #cfcfcf; }
  .newsletter .subscribe { position: absolute; left: 79px; top: 155px; width: 92px; height: 24px; background: var(--navy); color: var(--white); font-weight: 700; font-size: 13px; text-align: center; line-height: 24px; }

  /* Footer */
  .footer-rule { left: 62px; top: 1108px; width: 836px; height: 1px; background: var(--rule); }
  .footer-nav a { position: absolute; top: 1120px; font-family: "Cantarell", sans-serif; font-size: 13.5px; color: #666; text-decoration: none; }
  .copyright { left: 72px; top: 1157px; font-size: 10px; color: var(--muted); }
  .copyright b { color: var(--navy-text); }
  .social { position: absolute; top: 1145px; width: 40px; height: 40px; border-radius: 50%; border: 2px solid var(--navy); color: var(--navy-text); font-size: 8.5px; text-align: center; line-height: 36px; }
</style>
</head>
<body>

<header>
  <div class="abs brand-mark"></div>
  <div class="abs brand-name">R7 GROUP</div>

  <nav class="abs main-nav">
    <a class="current" style="left:16px">About Us</a>
    <a style="left:110px">Services</a>
    <a style="left:196px">Careers</a>
    <a style="left:280px">Contracts</a>
    <a style="left:374px">Contact</a>
    <div class="search">
      <svg width="15" height="15" viewBox="0 0 16 16"><circle cx="6.5" cy="6.5" r="5" fill="none" stroke="#333" stroke-width="2"/><line x1="10" y1="10" x2="15" y2="15" stroke="#333" stroke-width="2.4" stroke-linecap="round"/></svg>
      <span>Search here...</span>
    </div>
  </nav>
</header>

<section class="abs hero" role="img" aria-label="Snow-covered mountain peak under a blue sky with clouds">
  <h1 class="hero-title">SECURING THE CONTINUUM</h1>
  <div class="hero-rule"></div>
  <p class="hero-text lines">Lorem Ipsum is simply dummy text of the printing and<br>typesetting industry. Lorem Ipsum has been the industry's<br>standard dummy text ever since the 1500sLorem Ipsum.</p>
  <svg class="hero-arrow" style="left:12px" width="24" height="54" viewBox="0 0 24 54"><polyline points="22,2 2,27 22,52" fill="none" stroke="#fff" stroke-width="2"/></svg>
  <svg class="hero-arrow" style="left:800px" width="24" height="54" viewBox="0 0 24 54"><polyline points="2,2 22,27 2,52" fill="none" stroke="#fff" stroke-width="2"/></svg>
  <div class="hero-dots"><span class="active"></span><span></span><span></span><span></span></div>
</section>

<main>
  <h2 class="abs heading welcome-title">Welcome to R7 GROUP</h2>
  <p class="abs welcome-text lines">Lorem Ipsum is simply dummy text of the printing and typesetting industry. Lorem Ipsum has been the industry's<br>standard dummy text ever since the 1500s, when an unknown printer took a galley of type and scrambled it to<br>make a type specimen book. It has survived not only five centuries, but also the leap into lectronic typesetting.</p>
  <p class="abs welcome-note lines">Lorem Ipsum is simply dummy text of the printing and typesetting industry. Lorem Ipsum has been the industry's<br>standard dummy text ever since the 1500s, when an unknown printer took a galley of type.</p>

  <section class="abs features">
    <h2 class="heading features-title">Features</h2>

    <div class="feature-photo" style="left:8px"><div class="photo-security" role="img" aria-label="Padlock on a glowing blue circuit board"></div></div>
    <h3 class="heading feature-title" style="left:201px">Technology Integration</h3>
    <p class="feature-text lines" style="left:202px">Lorem Ipsum is simply dummy text of the<br>printing and typesetting industry. Lorem<br>Ipsum has been the industry's standard<br>dummy text ever since the 1500s</p>
    <div class="read-more" style="left:200px">READ MORE</div>

    <div class="feature-photo" style="left:419px"><div class="photo-meeting" role="img" aria-label="Business team reviewing documents at a meeting"></div></div>
    <h3 class="heading feature-title" style="left:615px">Case Study</h3>
    <p class="feature-text lines" style="left:616px">Lorem Ipsum is simply dummy text of the<br>printing and typesetting industry. Lorem<br>Ipsum has been the industry's standard<br>dummy text ever since the 1500s</p>
    <div class="read-more" style="left:615px">READ MORE</div>
  </section>

  <h2 class="abs heading news-title">Latest News</h2>
  <ul class="abs news-list">
    <li><span class="news-date">Dec 17 2014</span><span class="news-text">Lorem Ipsum is simply dummy text of the printing and typesetting industry. Lorem Ipsum has been the industry's standard dummy text ever since the 1500s.</span></li>
    <li><span class="news-date">Dec 14 2014</span><span class="news-text">Lorem Ipsum is simply dummy text of the printing and typesetting industry. Lorem Ipsum has been the industry's standard dummy text ever since the 1500s.</span></li>
    <li><span class="news-date">Dec 10 2014</span><span class="news-text">Lorem Ipsum is simply dummy text of the printing and typesetting industry.</span></li>
    <li><span class="news-date">Dec 10 2014</span><span class="news-text">Lorem Ipsum is simply dummy text of the printing and typesetting industry.</span></li>
  </ul>

  <aside class="abs newsletter">
    <h2 class="heading">Subscribe to newsletter</h2>
    <label style="top:47px">Enter your name</label>
    <div class="field" style="top:64px"></div>
    <label style="top:100px">Enter your Email</label>
    <div class="field" style="top:116px"></div>
    <div class="subscribe">Subscribe</div>
  </aside>
</main>

<footer>
  <div class="abs footer-rule"></div>
  <nav class="footer-nav">
    <a style="left:245px">About Us</a>
    <a style="left:356px">Services</a>
    <a style="left:458px">Careers</a>
    <a style="left:558px">Contracts</a>
    <a style="left:669px">Contact</a>
  </nav>
  <p class="abs copyright">© <b>R7 GROUP</b> - 2014. All Rights Reserved.</p>
  <div class="social" style="left:733px">Pals</div>
  <div class="social" style="left:792px">Chirp</div>
  <div class="social" style="left:850px">Joblink</div>
</footer>

</body>
</html>
```